Law Firm Redesign of Stationery

We are a law firm that just expanded to our second location. We had a redesign on our logo for signage and we are now looking for a redesign of business cards (updated for our 6 current staff), letterhead, and envelopes for the new logo and include both locations. We have the Illustrator file for the new logo and the Illustrator or EPS files for all previous stationery. We would like to keep the same blue/gray color scheme but try and find a new look that matches the new logo. Our locations are in the Baltimore/D.C. metro area so something fresh, professional, and urban is the direction we would like to go in.
Industry/Entity Type
Legal
Requirements
Must have
- Must have both office addresses included: 415 Pellmore Rd, N.W., Ashvale, MD 20999 and 5183 Thistlebend Lane, Brennick, MD 20988. We would like to maintain the current blue and grey color scheme.

```html
<!DOCTYPE html>
<html lang="en">
<head>
<meta charset="utf-8">
<title>Hale &amp; Co Law — Business Card</title>
<link rel="stylesheet" href="https://fonts.googleapis.com/css2?family=Arimo:wght@400;700&display=swap">
<style>
  :root {
    --backdrop: #2b2b2d;
    --card: #0c0c0d;
    --brand-blue: #1565c0;
    --rule-gray: #6e6e72;
    --text-light: #d9d9dc;
    --divider: #3a3a3e;
  }
  * { box-sizing: border-box; margin: 0; padding: 0; }
  html, body {
    width: 1200px; height: 900px; overflow: hidden;
    background: var(--backdrop);
    font-family: "Arimo", Arial, sans-serif;
  }
  .canvas {
    width: 1200px; height: 900px;
    display: flex; flex-direction: column; align-items: center; justify-content: center;
    gap: 40px;
  }
  .card {
    position: relative;
    width: 680px; height: 388px;
    background: var(--card);
    box-shadow: 0 12px 30px rgba(0,0,0,.5);
  }
  .rule {
    position: absolute; height: 6px;
    border-top: 2px solid var(--brand-blue);
    border-bottom: 2px solid var(--rule-gray);
  }
  .wordmark {
    position: absolute;
    color: var(--brand-blue);
    font-weight: 400;
    letter-spacing: 1px;
    white-space: nowrap;
  }
  .card-front .rule-top { left: 40px; width: 320px; top: 112px; }
  .card-front .rule-bottom { left: 70px; width: 320px; top: 268px; }
  .card-front .wordmark { left: 40px; width: 350px; text-align: center; top: 166px; font-size: 40px; }
  .divider {
    position: absolute; left: 420px; top: 82px; width: 1px; height: 240px;
    background: var(--divider);
  }
  .contact { position: absolute; left: 442px; top: 70px; color: var(--text-light); font-size: 15px; line-height: 1.3; }
  .person-name { color: var(--brand-blue); font-weight: 700; font-size: 17px; text-transform: uppercase; letter-spacing: .5px; }
  .person-title { margin-bottom: 6px; }
  .contact-list { list-style: none; margin-bottom: 12px; }
  .contact-list li { display: flex; align-items: center; gap: 8px; }
  .contact-list svg { width: 13px; height: 13px; fill: var(--brand-blue); flex: none; }
  .web-domain { color: var(--brand-blue); }
  .office { margin-bottom: 10px; }
  .card-back .rule-top { left: 170px; width: 340px; top: 120px; }
  .card-back .rule-bottom { left: 200px; width: 340px; top: 262px; }
  .card-back .wordmark { left: 0; right: 0; text-align: center; top: 166px; font-size: 46px; }
</style>
</head>
<body>
<main class="canvas">
  <section class="card card-front">
    <div class="rule rule-top"></div>
    <div class="wordmark">HALE &amp; CO LAW</div>
    <div class="rule rule-bottom"></div>
    <div class="divider"></div>
    <div class="contact">
      <p class="person-name">Dana R. Mellor</p>
      <p class="person-title">Office Manager</p>
      <ul class="contact-list">
        <li><svg viewBox="0 0 16 16" aria-hidden="true"><path d="M3.6 1.2l2.3 2.9-1.3 1.6c.9 2 2.6 3.7 4.6 4.6l1.6-1.3 2.9 2.3-1.5 2.5C7 13.5 2.5 9 1.2 2.7z"/></svg><span>410-555-0142</span></li>
        <li><svg viewBox="0 0 16 16" aria-hidden="true"><path d="M4 1h8v4H4zM1 6h14v6h-3v3H4v-3H1zm4 4v4h6v-4z"/></svg><span>410-555-0187</span></li>
        <li><svg viewBox="0 0 16 16" aria-hidden="true"><path d="M1 3h14v10H1zm1.5 1.2L8 8.5l5.5-4.3z"/></svg><span>dmellor@halecolaw.com</span></li>
        <li><svg viewBox="0 0 16 16" aria-hidden="true"><path d="M8 1a7 7 0 100 14A7 7 0 008 1zm-1 1.6v2.4H4.4A5.6 5.6 0 017 2.6zm2 0a5.6 5.6 0 012.6 2.4H9zM3.5 7h3.5v2H3.5a5 5 0 010-2zm5.5 0h3.5a5 5 0 010 2H9zm-4.6 4H7v2.4A5.6 5.6 0 014.4 11zM9 11h2.6A5.6 5.6 0 019 13.4z"/></svg><span>www.<span class="web-domain">halecolaw</span>.com</span></li>
      </ul>
      <p class="office">415 Pellmore Rd, N.W.,<br>Ashvale, MD 20999</p>
      <p class="office">5183 Thistlebend Lane<br>Brennick, MD 20988.</p>
    </div>
  </section>
  <section class="card card-back">
    <div class="rule rule-top"></div>
    <div class="wordmark">HALE &amp; CO LAW</div>
    <div class="rule rule-bottom"></div>
  </section>
</main>
</body>
</html>
```